Real Estate Flyer

Hi - I am assisting a relative to sell a unit. I am looking to have a two page flyer designed (configured as a single page with back to back printing). I have uploaded two samples to give you an idea of the look and feel - one which relates to this property when originally purchased, the other for a different property.
The flyer should includes several key photos on the front along with the wording. The rear should include any secondary photos along with the floor plan.
The flyer should be close to A4 size.

Updates
Hi,
Industry/Entity Type
Real Estate
Look and feel
Each slider illustrates characteristics of the customer's brand and the style your logo design should communicate.

```html
<!DOCTYPE html>
<html lang="en">
<head>
<meta charset="utf-8">
<title>Eastmere Apartment Flyer</title>
<link rel="stylesheet" href="https://fonts.googleapis.com/css2?family=Archivo:wght@700;800&family=Arimo:wght@400;700&display=swap">
<style>
  :root {
    --brand-blue: #1c33d4;
    --paper: #ffffff;
    --frame: #3a3a3a;
    --canvas-bg: #ffffff;
    --photo-sky: #8fb6df;
    --photo-brick: #b05a42;
    --photo-pool: #3fc4c9;
    --photo-cream: #e9e3d5;
    --photo-carpet: #8a847c;
    --photo-tile: #dfe7e4;
    --plan-paper: #f3f3f3;
  }
  * { box-sizing: border-box; margin: 0; padding: 0; }
  html, body { width: 1200px; height: 805px; overflow: hidden; background: var(--canvas-bg); }
  body { position: relative; font-family: "Arimo", Arial, sans-serif; color: var(--brand-blue); }

  .page { position: absolute; top: 56px; width: 497px; height: 703px; background: var(--paper); border: 1px solid var(--frame); overflow: hidden; }
  .page--front { left: 84px; }
  .page--back { left: 629px; }

  .photo { position: absolute; }

  /* Front */
  .front-title { position: absolute; top: 16px; left: 0; width: 100%; text-align: center;
    font-family: "Archivo", Arial, sans-serif; font-weight: 800; font-size: 37px; line-height: 37px; letter-spacing: 0.2px; }
  .front-address { position: absolute; top: 95px; width: 100%; text-align: center; font-weight: 700; font-size: 17px; }
  .front-specs { position: absolute; top: 118px; width: 100%; text-align: center; font-size: 16px; }
  .photo--balcony { left: 0; top: 148px; width: 251px; height: 170px; background: linear-gradient(120deg, var(--photo-cream) 0%, #c9a48a 45%, var(--photo-brick) 65%, var(--photo-sky) 100%); }
  .photo--living { left: 258px; top: 148px; width: 239px; height: 170px; background: linear-gradient(180deg, #f2efe6 0%, var(--photo-cream) 60%, var(--photo-carpet) 100%); }
  .photo--building { left: 0; top: 324px; width: 497px; height: 379px; background: linear-gradient(180deg, var(--photo-sky) 0%, var(--photo-brick) 30%, #a9523c 60%, #d9c4ad 75%, var(--photo-pool) 100%); }

  /* Back */
  .photo--bathroom { left: 0; top: 11px; width: 246px; height: 170px; background: linear-gradient(100deg, #d7dcd6 0%, var(--photo-tile) 50%, #f4f4f2 100%); }
  .photo--kitchen { left: 251px; top: 11px; width: 210px; height: 170px; background: linear-gradient(180deg, #efece4 0%, var(--photo-cream) 70%, #6a4a44 100%); }
  .photo--oven { left: 464px; top: 11px; width: 33px; height: 170px; background: linear-gradient(180deg, #f4f4f2 0%, #d8d8d4 50%, #333 100%); }

  .back-heading { position: absolute; top: 205px; width: 100%; text-align: center; font-weight: 700; font-size: 17px; }
  .back-specs { position: absolute; top: 229px; width: 100%; text-align: center; font-size: 15px; }
  .back-address { position: absolute; top: 250px; width: 100%; text-align: center; font-weight: 700; font-size: 15px; }
  .intro { position: absolute; top: 273px; left: 38px; width: 424px; text-align: center; font-size: 11px; line-height: 12.6px; }
  .intro sup { font-size: 7px; }

  .floor-plan { position: absolute; left: 23px; top: 352px; width: 214px; height: 278px; background: var(--plan-paper); border: 1px solid #cfcfcf; }

  .features { position: absolute; left: 254px; top: 358px; width: 240px; list-style: none; font-size: 10.2px; line-height: 18.6px; }
  .features li { padding-left: 7px; text-indent: -7px; }
  .features li::before { content: "• "; }

  .rates { position: absolute; left: 254px; top: 505px; font-size: 10.2px; line-height: 18.4px; }

  .inspect { position: absolute; top: 634px; width: 100%; text-align: center; font-size: 8.6px; }
  .contact { position: absolute; top: 648px; width: 100%; text-align: center; font-weight: 700; font-size: 13.6px; }
  .phone { position: absolute; top: 667px; width: 100%; text-align: center; font-weight: 700; font-size: 18px; }
</style>
</head>
<body>
  <section class="page page--front">
    <h1 class="front-title">Oversized apartment<br>in a lifestyle location.</h1>
    <p class="front-address">8/41-47 Harbour Lane, Eastmere</p>
    <p class="front-specs">2 BED | 1 BATH | 1 CAR</p>
    <div class="photo photo--balcony" role="img" aria-label="Photo of the curved balcony terrace looking back into the apartment"></div>
    <div class="photo photo--living" role="img" aria-label="Photo of the empty open plan living room"></div>
    <div class="photo photo--building" role="img" aria-label="Photo of the brick apartment building with curved balconies above the outdoor pool"></div>
  </section>

  <section class="page page--back">
    <div class="photo photo--bathroom" role="img" aria-label="Photo of the tiled bathroom with vanity and glass shower"></div>
    <div class="photo photo--kitchen" role="img" aria-label="Photo of the white kitchen with gas cooktop"></div>
    <div class="photo photo--oven" role="img" aria-label="Photo of the wall oven"></div>

    <h2 class="back-heading">Oversized apartment in a lifestyle location.</h2>
    <p class="back-specs">2 BED | 1 BATH | 1 CAR</p>
    <p class="back-address">8/41-47 Harbour Lane, EASTMERE</p>
    <p class="intro">Peacefully positioned on the 5<sup>th</sup> floor of a refurbished security building, this superbly spacious residence combines modern, low maintenance apartment living with inviting prospects for the entertainer. Boasting a huge full-width terrace on-title, its sought-after setting in the heart of Eastmere offers the ultimate in lifestyle and convenience.</p>

    <div class="floor-plan" role="img" aria-label="Floor plan of level five: two balconies, main bedroom, bedroom 2, kitchen, living and dining, bathroom, ensuite, laundry and car space"></div>

    <ul class="features">
      <li>Expansive open plan living and dining area</li>
      <li>Terrace features city and Southbay glimpses</li>
      <li>Kitchen updated with Corvo gas appliances</li>
      <li>Built-ins in both bedrooms, fully tiled bathrooms</li>
      <li>Internal laundry, secure parking, lift, outdoor pool and gymnasium</li>
      <li>Steps to station, Parkside Mall and Greenfield Park</li>
    </ul>

    <p class="rates">Water Rates:<br>Council Rates:<br>Strata Rates:<br>Estimated Market Rental: $700.00 p/w</p>

    <p class="inspect">Inspect : Sat 10:45 – 11:30; Wed 12:00 – 12:30</p>
    <p class="contact">Contact:&nbsp; Tom Hartley (Assisting owner in Private Sale)</p>
    <p class="phone">0412 555 018</p>
  </section>
</body>
</html>
```